Design for an iOS and Android app managing shopping list

The app allows you to keep manage shopping lists, each shopping list being made of items to buy...
We need a design for the 3 screens of the app:
a) global view showing list of (shopping) list
b) form enabling to edit the name of a (shopping) list
c) detailed view listing the contents/items of a (shopping) list
d) 1 text page [not illustrated]
2 "alerts" items are also to be designed: confirm and error pop ups.
No specific guidelines, nor logo or whatever.
It will be a free app distributed on iOS and Androïd.
We just want to make it looking nice & very usable for end users.

```html
<!DOCTYPE html>
<html lang="en">
<head>
<meta charset="utf-8">
<title>Home – Shopping Lists</title>
<link href="https://fonts.googleapis.com/css2?family=Hind:wght@300;400;500&display=swap" rel="stylesheet">
<style>
  :root {
    --status-bg: #56666f;
    --header-bg: #62777f;
    --header-deep: #56686f;
    --search-bg: #ffffff;
    --search-hint: #b9c0c4;
    --search-icon: #6f7b82;
    --favs-bg: #2a343b;
    --recent-bg: #34434b;
    --tile-red: #ee5455;
    --tile-teal: #26a698;
    --text-light: #ffffff;
    --text-soft: #e6ecef;
  }
  * { margin: 0; padding: 0; box-sizing: border-box; }
  html, body {
    width: 750px; height: 1200px; overflow: hidden;
    background: var(--favs-bg);
    font-family: "Hind", sans-serif;
  }
  .screen { position: relative; width: 750px; height: 1200px; overflow: hidden; }

  .status-bar {
    position: absolute; left: 0; top: 0; width: 750px; height: 57px;
    background: var(--status-bg);
    display: flex; align-items: center; justify-content: flex-end;
    gap: 10px; padding-right: 14px;
    color: var(--text-light); font-weight: 500; font-size: 27px;
  }
  .status-bar span { padding-top: 5px; }
  .status-bar svg { display: block; }

  .app-header {
    position: absolute; left: 0; top: 57px; width: 750px; height: 287px;
    background: linear-gradient(180deg, var(--header-bg) 0%, var(--header-deep) 100%);
  }
  .menu-button { position: absolute; left: 40px; top: 49px; }
  .screen-title {
    position: absolute; left: 127px; top: 38px;
    font-size: 46px; font-weight: 500; color: var(--text-light); line-height: 1.2;
  }
  .header-art {
    position: absolute; left: 450px; top: 0; width: 200px; height: 152px;
    background:
      radial-gradient(ellipse 40% 28% at 40% 88%, rgba(232, 196, 140, 0.55), rgba(232, 196, 140, 0) 100%),
      radial-gradient(ellipse 55% 55% at 45% 70%, rgba(170, 190, 205, 0.55), rgba(170, 190, 205, 0) 100%);
  }
  .chat-button { position: absolute; right: 22px; top: 40px; }

  .search-field {
    position: absolute; left: 25px; top: 152px; width: 704px; height: 108px;
    background: var(--search-bg); border-radius: 3px;
    display: flex; align-items: center; gap: 28px; padding-left: 30px;
    box-shadow: 0 2px 4px rgba(0,0,0,0.15);
  }
  .search-field span { font-size: 33px; font-weight: 300; color: var(--search-hint); padding-top: 6px; }

  .favourites {
    position: absolute; left: 0; top: 344px; width: 750px; height: 317px;
    background: var(--favs-bg);
  }
  .recent {
    position: absolute; left: 0; top: 661px; width: 750px; height: 539px;
    background: var(--recent-bg);
  }
  .section-title {
    position: absolute; left: 52px; top: 30px;
    font-size: 48px; font-weight: 300; color: var(--text-soft); line-height: 1.2;
  }
  .collapse-button { position: absolute; right: 58px; top: 48px; }

  .tile { position: absolute; width: 228px; height: 258px; }
  .tile-red { background: var(--tile-red); }
  .tile-teal { background: var(--tile-teal); }
  .tile-art {
    position: absolute; left: 39px; top: 28px; width: 150px; height: 136px;
    background: radial-gradient(circle at 50% 50%, rgba(255,255,255,0.16) 0%, rgba(255,255,255,0.06) 45%, rgba(255,255,255,0) 70%);
  }
  .tile-label {
    position: absolute; left: 0; right: 0; top: 194px;
    text-align: center; font-size: 34px; font-weight: 400;
    color: var(--text-light); line-height: 1;
  }
</style>
</head>
<body>
<main class="screen">

  <div class="status-bar">
    <svg width="46" height="30" viewBox="0 0 46 30" aria-hidden="true">
      <text x="0" y="11" font-size="12" font-family="Hind, sans-serif" font-weight="500" fill="#fff">3G</text>
      <path d="M14 28 L40 2 L40 28 Z" fill="#fff"/>
    </svg>
    <svg width="20" height="30" viewBox="0 0 20 30" aria-hidden="true">
      <rect x="2" y="2" width="16" height="26" rx="2" fill="#fff"/>
    </svg>
    <span>7:48</span>
  </div>

  <header class="app-header">
    <svg class="menu-button" width="40" height="30" viewBox="0 0 40 30" aria-label="Menu">
      <rect x="0" y="1" width="40" height="4" fill="#fff"/>
      <rect x="0" y="13" width="40" height="4" fill="#fff"/>
      <rect x="0" y="25" width="40" height="4" fill="#fff"/>
    </svg>
    <h1 class="screen-title">Home</h1>
    <div class="header-art" role="img" aria-label="Illustration of a milk carton, a loaf of bread and a steaming pot"></div>
    <svg class="chat-button" width="44" height="44" viewBox="0 0 44 44" aria-label="Messages">
      <path d="M4 3 H40 A2 2 0 0 1 42 5 V31 A2 2 0 0 1 40 33 H12 L4 41 Z" fill="#fff"/>
      <circle cx="14" cy="18" r="2.6" fill="#5f7581"/>
      <circle cx="23" cy="18" r="2.6" fill="#5f7581"/>
      <circle cx="32" cy="18" r="2.6" fill="#5f7581"/>
    </svg>

    <label class="search-field">
      <svg width="38" height="38" viewBox="0 0 36 36" aria-hidden="true">
        <circle cx="14" cy="14" r="11" fill="none" stroke="#6f7b82" stroke-width="4"/>
        <line x1="22" y1="22" x2="33" y2="33" stroke="#6f7b82" stroke-width="4.5" stroke-linecap="round"/>
      </svg>
      <span>What would you like to buy?</span>
    </label>
  </header>

  <section class="favourites">
    <div class="tile tile-red" style="left:29px; top:31px;">
      <div class="tile-art" role="img" aria-label="Line drawing of a loaf of bread"></div>
      <span class="tile-label">Bread</span>
    </div>
    <div class="tile tile-red" style="left:263px; top:31px;">
      <div class="tile-art" role="img" aria-label="Line drawing of a milk carton"></div>
      <span class="tile-label">Milk</span>
    </div>
  </section>

  <section class="recent">
    <h2 class="section-title">Recently Used</h2>
    <svg class="collapse-button" width="28" height="18" viewBox="0 0 28 18" aria-label="Collapse">
      <path d="M3 15 L14 4 L25 15" fill="none" stroke="#fff" stroke-width="4.5" stroke-linecap="round" stroke-linejoin="round"/>
    </svg>

    <div class="tile tile-teal" style="left:29px; top:114px;">
      <div class="tile-art" role="img" aria-label="Line drawing of carrots"></div>
      <span class="tile-label">Carrots</span>
    </div>
    <div class="tile tile-teal" style="left:263px; top:114px;">
      <div class="tile-art" role="img" aria-label="Line drawing of bananas"></div>
      <span class="tile-label">Bananas</span>
    </div>
    <div class="tile tile-teal" style="left:498px; top:114px;">
      <div class="tile-art" role="img" aria-label="Line drawing of an apple"></div>
      <span class="tile-label">Apples</span>
    </div>

    <div class="tile tile-teal" style="left:29px; top:379px;">
      <div class="tile-art" role="img" aria-label="Line drawing of eggs"></div>
      <span class="tile-label">Eggs</span>
    </div>
    <div class="tile tile-teal" style="left:263px; top:379px;">
      <div class="tile-art" role="img" aria-label="Line drawing of cheese"></div>
      <span class="tile-label">Cheese</span>
    </div>
    <div class="tile tile-teal" style="left:498px; top:379px;">
      <div class="tile-art" role="img" aria-label="Line drawing of a yogurt cup"></div>
      <span class="tile-label">Yogurt</span>
    </div>

    <div class="tile tile-teal" style="left:29px; top:644px;"></div>
    <div class="tile tile-teal" style="left:263px; top:644px;"></div>
    <div class="tile tile-teal" style="left:498px; top:644px;"></div>
  </section>

</main>
</body>
</html>
```